Zaberu - Wordpress website for hot new GIF booth

We need a responsive website for a new brand we're launching. Scrolling parallax style. We are a event photo company offering the hottest new GIF booths. We want our site to be sleek, sexy, moving.

Here's some sites we like:
https://www.tundrix.com/us/
http://kelvasnap.com/
http://lark9.drumvelisaphone.com/

Target Market(s)

advertising agencies, marketing agencies, major brands, corporate planners, millenials

Industry/Entity Type

Events

Number of Pages Required

1 page

Font styles to use
Sans Serif

Colors
33b8a4
86cfc6
ffffff

Requirements
Must have
• I want it very much like this: https://www.tundrix.com/us/
• lots of imagery, movement
• Here's some competitors:
• http://www.quellarix.com/
• http://runbrightwick.com/
• http://www.dqrstudio.com/gif-photo-booth-rental/
• http://kelvasnap.com/
Nice to have
• slider at top with different booth designs
Should not have
• no bulky tabs at top

```html
<!DOCTYPE html>
<html lang="en">
<head>
<meta charset="utf-8">
<title>Zaberu — GIF Booths</title>
<link href="https://fonts.googleapis.com/css2?family=Open+Sans:wght@400;600;700&display=swap" rel="stylesheet">
<style>
:root{
  --teal:#33b8a4;
  --teal-soft:#86cfc6;
  --teal-deep:#1f8f88;
  --white:#ffffff;
  --ink:#4a4f5c;
  --muted:#8a8f99;
  --nav:#e6e8ea;
  --footer:#2c3146;
  --footer-panel:#353b52;
  --footer-text:#b9bdc9;
}
*{box-sizing:border-box;margin:0;padding:0}
html,body{width:1200px;height:2452px;overflow:hidden;background:var(--white);font-family:"Open Sans",Arial,sans-serif;color:var(--ink)}
.page{position:relative;width:1200px;height:2452px}

/* hero */
.hero{position:absolute;left:0;top:0;width:1200px;height:500px;overflow:hidden}
.hero-media{position:absolute;inset:0;background:linear-gradient(120deg,#3b7f86 0%,#5fb3ae 35%,#7cc7bf 55%,#4a9aa0 80%,#2f6f78 100%)}
.hero-tint{position:absolute;inset:0;background:linear-gradient(180deg,rgba(51,184,164,.35),rgba(31,143,136,.55))}
.brand{position:absolute;left:40px;top:22px;display:flex;align-items:center;gap:10px;font-weight:700;font-size:30px;color:var(--white);letter-spacing:1px}
.brand-mark{width:26px;height:26px;background:var(--white)}
.account{position:absolute;right:70px;top:30px;display:flex;gap:22px}
.pill{width:96px;height:30px;border-radius:15px;background:var(--white);color:var(--teal);font-size:13px;font-weight:600;display:flex;align-items:center;justify-content:center}
.hero-title{position:absolute;left:0;top:178px;width:1200px;text-align:center;color:var(--white);font-size:40px;font-weight:600;line-height:54px}
.hero-btn{position:absolute;left:512px;top:346px;width:176px;height:52px;border:2px solid var(--white);border-radius:26px;color:var(--white);font-size:15px;display:flex;align-items:center;justify-content:center}

/* nav */
.nav{position:absolute;left:0;top:500px;width:1200px;height:50px;background:var(--nav);display:flex;padding-left:360px}
.nav a{display:flex;align-items:center;padding:0 18px;font-size:14px;color:var(--ink);text-decoration:none}
.nav a.active{background:var(--teal);color:var(--white)}

/* features */
.booth{position:absolute;left:520px;top:588px;width:160px;height:405px;border-radius:10px 10px 6px 6px;background:linear-gradient(180deg,#1b1c20 0%,#2e3035 40%,#e9ebee 60%,#c6c9ce 100%)}
.feature{position:absolute;width:340px}
.feature h3{font-size:17px;font-weight:600;color:var(--teal-deep);margin-bottom:14px}
.feature p{font-size:11.5px;line-height:17px;color:var(--muted)}
.feature.left{left:150px}
.feature.right{left:790px}
.feature.right h3{padding-left:56px}
.connector{position:absolute;height:16px}

/* testimonial */
.testimonial{position:absolute;left:0;top:1020px;width:1200px;height:390px;background:linear-gradient(160deg,var(--teal-soft) 0%,var(--teal) 50%,var(--teal-deep) 100%)}
.quote-badge{position:absolute;left:563px;top:28px;width:74px;height:74px;border-radius:50%;background:rgba(255,255,255,.22);display:flex;align-items:center;justify-content:center}
.avatar{position:absolute;left:205px;top:200px;width:112px;height:112px;border-radius:50%;border:4px solid var(--white);background:linear-gradient(160deg,#e7c6a8,#b28a6c)}
.quote{position:absolute;left:345px;top:212px;width:590px;color:var(--white);font-size:12.5px;line-height:18px}
.quote cite{display:block;margin-top:8px;font-style:normal;font-weight:600}

/* gallery */
.section-title{position:absolute;left:0;top:1462px;width:1200px;text-align:center;font-size:30px;font-weight:600;color:var(--teal-deep)}
.section-rule{position:absolute;left:560px;top:1512px;width:80px;height:2px;background:var(--teal)}
.gallery{position:absolute;left:100px;top:1540px;width:1000px;display:grid;grid-template-columns:repeat(4,232px);grid-auto-rows:185px;column-gap:24px;row-gap:22px}
.tile{border-radius:4px}
.t1{background:linear-gradient(150deg,#c23a3a,#7a1f2a)}
.t2{background:linear-gradient(150deg,#f1efec,#b9b4ae)}
.t3{background:linear-gradient(150deg,#6c6760,#2f2c29)}
.t4{background:linear-gradient(150deg,#4a4e5a,#16181d)}
.t5{background:linear-gradient(150deg,#3e8fc9,#d14a7a)}
.t6{background:linear-gradient(150deg,#d9d6d2,#8e8781)}
.t7{background:linear-gradient(150deg,#b47a56,#4d2d22)}
.t8{background:linear-gradient(150deg,#e3c2c6,#a06f7e)}
.view-all{position:absolute;left:500px;top:1950px;width:200px;height:48px;border:2px solid var(--teal);border-radius:24px;color:var(--teal);font-size:15px;display:flex;align-items:center;justify-content:center}

/* footer */
.footer{position:absolute;left:0;top:2040px;width:1200px;height:412px;background:var(--footer)}
.footer-panel{position:absolute;left:80px;top:0;width:240px;height:372px;background:var(--footer-panel)}
.footer-brand{position:absolute;left:20px;top:30px;width:190px;height:86px;background:var(--white);display:flex;align-items:center;justify-content:center;gap:10px;font-size:28px;font-weight:700;color:var(--footer)}
.footer-brand span.sq{width:22px;height:22px;background:var(--footer)}
.footer-about{position:absolute;left:24px;top:140px;width:196px;font-size:12px;line-height:18px;color:var(--footer-text)}
.contact{position:absolute;left:24px;top:226px;font-size:10.5px;line-height:20px;color:var(--footer-text)}
.contact div{display:flex;align-items:center;gap:8px}
.fcol{position:absolute;top:40px}
.fcol-head{display:flex;gap:12px;align-items:flex-start}
.ficon{width:34px;height:34px;border-radius:50%;background:var(--white);flex:none;display:flex;align-items:center;justify-content:center}
.fcol h4{font-size:14px;font-weight:600;color:var(--teal-soft);line-height:17px}
.fcol small{display:block;font-size:10px;color:var(--footer-text);margin-top:3px}
.fimg{position:absolute;border-radius:2px}
.ftext{position:absolute;font-size:12px;line-height:17px;color:var(--footer-text)}
.subscribe{display:flex;margin-top:16px}
.subscribe .field{width:150px;height:30px;background:var(--white);font-size:11px;color:var(--ink);padding:7px 8px}
.subscribe .go{width:30px;height:30px;background:var(--teal)}
.socials{display:flex;gap:8px;margin-top:16px}
.socials span{width:26px;height:26px;border-radius:3px}
.copyright{position:absolute;left:0;top:372px;width:1200px;height:40px;display:flex;align-items:center;justify-content:center;font-size:11px;color:var(--footer-text);border-top:1px solid #3d4360}
</style>
</head>
<body>
<div class="page">

  <header class="hero">
    <div class="hero-media" role="img" aria-label="Collage of event guests posing at a photo booth"></div>
    <div class="hero-tint"></div>
    <div class="brand"><span class="brand-mark"></span>Zaberu</div>
    <div class="account"><span class="pill">Sign Up</span><span class="pill">Login</span></div>
    <h1 class="hero-title">Social Photo and Video Solutions<br>For Live Experiences</h1>
    <div class="hero-btn">Read More</div>
  </header>

  <nav class="nav">
    <a class="active">Home</a><a>About</a><a>Gallery</a><a>Testimonials</a><a>Contact</a>
  </nav>

  <section class="features">
    <div class="booth" role="img" aria-label="Free-standing GIF photo booth kiosk"></div>

    <div class="feature left" style="top:620px">
      <h3>The Animated Gif Booth</h3>
      <p>Guests step up, strike a pose and get a looping clip in seconds. Our booth shares every moment straight to phones, screens and social feeds while the party keeps going all night.</p>
    </div>
    <svg class="connector" style="left:360px;top:625px" width="140" height="16"><line x1="0" y1="8" x2="126" y2="8" stroke="#33b8a4" stroke-width="2"/><circle cx="132" cy="8" r="6" fill="#fff" stroke="#33b8a4" stroke-width="2"/></svg>

    <div class="feature left" style="top:844px">
      <h3>The Animated Gif Booth</h3>
      <p>Guests step up, strike a pose and get a looping clip in seconds. Our booth shares every moment straight to phones, screens and social feeds while the party keeps going all night.</p>
    </div>
    <svg class="connector" style="left:360px;top:849px" width="140" height="16"><line x1="0" y1="8" x2="126" y2="8" stroke="#33b8a4" stroke-width="2"/><circle cx="132" cy="8" r="6" fill="#fff" stroke="#33b8a4" stroke-width="2"/></svg>

    <div class="feature right" style="top:620px">
      <h3>The Animated Gif Booth</h3>
      <p>Branded frames, custom overlays and instant sharing turn every guest into a promoter. Set up takes minutes and our friendly attendants handle the rest from start to finish.</p>
    </div>
    <svg class="connector" style="left:780px;top:625px" width="60" height="16"><circle cx="8" cy="8" r="6" fill="#fff" stroke="#33b8a4" stroke-width="2"/><line x1="14" y1="8" x2="56" y2="8" stroke="#33b8a4" stroke-width="2"/></svg>

    <div class="feature right" style="top:844px">
      <h3>The Animated Gif Booth</h3>
      <p>Branded frames, custom overlays and instant sharing turn every guest into a promoter. Set up takes minutes and our friendly attendants handle the rest from start to finish.</p>
    </div>
    <svg class="connector" style="left:780px;top:849px" width="60" height="16"><circle cx="8" cy="8" r="6" fill="#fff" stroke="#33b8a4" stroke-width="2"/><line x1="14" y1="8" x2="56" y2="8" stroke="#33b8a4" stroke-width="2"/></svg>
  </section>

  <section class="testimonial">
    <div class="quote-badge">
      <svg width="30" height="24" viewBox="0 0 30 24"><path d="M2 24V13C2 6 6 1 12 0v4c-3 1-5 4-5 8h5v12zM18 24V13c0-7 4-12 10-13v4c-3 1-5 4-5 8h5v12z" fill="#fff"/></svg>
    </div>
    <div class="avatar" role="img" aria-label="Portrait of a happy client"></div>
    <blockquote class="quote">
      The booth was the hit of our launch night. Guests lined up all evening, the clips looked amazing on the big screen and our social channels lit up within minutes. The team was friendly, fast and easy to work with from first call to last frame.
      <cite>— Lena Bay</cite>
    </blockquote>
  </section>

  <h2 class="section-title">Our Gallery</h2>
  <div class="section-rule"></div>
  <section class="gallery">
    <div class="tile t1" role="img" aria-label="Model in red dress"></div>
    <div class="tile t2" role="img" aria-label="Bride in white gown"></div>
    <div class="tile t3" role="img" aria-label="Dancer in motion"></div>
    <div class="tile t4" role="img" aria-label="Monochrome fashion portrait"></div>
    <div class="tile t5" role="img" aria-label="Colorful makeup portrait"></div>
    <div class="tile t6" role="img" aria-label="Soft fashion portrait"></div>
    <div class="tile t7" role="img" aria-label="Woman with curly hair"></div>
    <div class="tile t8" role="img" aria-label="Woman with pink hair"></div>
  </section>
  <div class="view-all">View All</div>

  <footer class="footer">
    <div class="footer-panel">
      <div class="footer-brand"><span class="sq"></span>Zaberu</div>
      <p class="footer-about">It is a long established fact that a guest will be thrilled by a booth that shares every moment.</p>
      <div class="contact">
        <div><svg width="10" height="12" viewBox="0 0 10 12"><path d="M5 0a4 4 0 0 0-4 4c0 3 4 8 4 8s4-5 4-8a4 4 0 0 0-4-4z" fill="#86cfc6"/></svg>120 Harbor Lane, Suite 4</div>
        <div><svg width="10" height="12" viewBox="0 0 10 12"><path d="M2 0h2l1 3-1.5 1a6 6 0 0 0 3 3L8 6l2 1v2c0 1-1 2-2 2C4 11 0 7 0 2 0 1 1 0 2 0z" fill="#86cfc6"/></svg>(555) 014-2290</div>
        <div><svg width="12" height="10" viewBox="0 0 12 10"><rect x="0" y="0" width="12" height="10" fill="#86cfc6"/><path d="M0 0l6 5 6-5" stroke="#353b52" fill="none"/></svg>hello@zaberu.com</div>
      </div>
    </div>

    <div class="fcol" style="left:360px;width:230px">
      <div class="fcol-head">
        <span class="ficon"><svg width="16" height="14" viewBox="0 0 16 14"><rect x="0" y="3" width="16" height="11" rx="2" fill="#2c3146"/><circle cx="8" cy="8.5" r="3" fill="#fff"/><rect x="5" y="0" width="6" height="3" fill="#2c3146"/></svg></span>
        <div><h4>The hottest new Gif booth</h4><small>two months ago</small></div>
      </div>
    </div>
    <div class="fimg" role="img" aria-label="Guests at an event" style="left:360px;top:92px;width:220px;height:100px;background:linear-gradient(150deg,#6a7080,#2e3240)"></div>
    <p class="ftext" style="left:360px;top:204px;width:220px">It is a long established fact that a guest will be charmed by a booth that keeps the fun rolling.</p>

    <div class="fcol" style="left:620px;width:220px">
      <div class="fcol-head">
        <span class="ficon"><svg width="16" height="14" viewBox="0 0 16 14"><rect x="0" y="0" width="16" height="14" rx="2" fill="#2c3146"/><path d="M2 12l4-5 3 3 2-2 3 4z" fill="#fff"/></svg></span>
        <div><h4>Photo Gallery</h4><small>all our best shots</small></div>
      </div>
    </div>
    <div class="fimg" role="img" aria-label="Event photo" style="left:620px;top:92px;width:95px;height:80px;background:linear-gradient(150deg,#8a7a70,#3a2f2a)"></div>
    <div class="fimg" role="img" aria-label="Event photo" style="left:722px;top:92px;width:95px;height:80px;background:linear-gradient(150deg,#c9b3a8,#6d5a52)"></div>
    <div class="fimg" role="img" aria-label="Event photo" style="left:620px;top:180px;width:95px;height:80px;background:linear-gradient(150deg,#9aa3b2,#4a5262)"></div>
    <div class="fimg" role="img" aria-label="Event photo" style="left:722px;top:180px;width:95px;height:80px;background:linear-gradient(150deg,#b08790,#5a3e46)"></div>

    <div class="fcol" style="left:875px;width:240px">
      <div class="fcol-head">
        <span class="ficon"><svg width="16" height="14" viewBox="0 0 16 14"><path d="M0 6L16 0 12 14 8 9z" fill="#2c3146"/></svg></span>
        <div><h4>Subscribe our Newsletter</h4><small>Simple updates, no spam</small></div>
      </div>
      <div class="subscribe"><span class="field">Enter Email</span><span class="go"></span></div>
      <div class="socials">
        <span style="background:var(--teal)"></span>
        <span style="background:var(--teal-soft)"></span>
        <span style="background:var(--teal-deep)"></span>
        <span style="background:var(--teal)"></span>
      </div>
    </div>

    <div class="copyright">Copyright © 2016</div>
  </footer>
</div>
</body>
</html>
```